In need of an AWESOME website for our Water Re-filling Store

The project is to design a website for our retail store front with the website www.brookvalerefillden.com. Currently if you go to that site it redirects you to our other site www.brookvalecanteenworks.com which is just our water bottle website. So, I need a new website created for www.brookvalerefillden.com (retail storefront)
Use our Squarespace to create a site with pages to help educate, tell about us, link to our water bottle brand site that is already created with Squarespace, and show the family and community aspects that we believe in. Our current water bottle website is www.brookvalecanteenworks.com for reference
We also sell hydration products, especially QZRV products and have access to digital media through our QZRV dealer site. we sell bottles, dispensers and other supplies for water refilling customers. We sell Ice as well.

Target Market(s)

Local residents looking to fill up their 1-5 gallon water jugs

Industry/Entity Type

Alkaline and Purified Water Retail Re-filling Store

Font styles to use
Serif
Sans Serif

Colors
0054AA
0677BA
7BADD7
CADEEF
E8F1F8

Requirements
Must have
• pictures of our family in the about us section and pictures of our store inside and out.

```html
<!DOCTYPE html>
<html lang="en">
<head>
<meta charset="utf-8">
<title>Brookvale Refill Den — Alkaline &amp; Purified Water</title>
<link href="https://fonts.googleapis.com/css2?family=Archivo:wght@400;500;600;700;800;900&display=swap" rel="stylesheet">
<style>
:root{
  --brand:#3a51a7;
  --brand-deep:#2f4393;
  --ink:#16171c;
  --text:#2b2d33;
  --footer:#24252d;
  --footer-line:#4a4c56;
  --pale:#eef1f8;
  --white:#ffffff;
}
*{box-sizing:border-box;margin:0;padding:0}
html,body{width:1200px;height:3436px;overflow:hidden}
body{position:relative;font-family:"Archivo",sans-serif;color:var(--text);background:var(--white)}
.abs{position:absolute}
.btn{position:absolute;display:flex;align-items:center;justify-content:center;border-radius:22px;background:var(--brand);color:var(--white);font-weight:800;font-size:11px;letter-spacing:.2px;text-transform:uppercase;text-decoration:none}

/* promo bar */
.promo-bar{left:0;top:0;width:1200px;height:24px;background:var(--brand);color:var(--white);font-size:10px;font-weight:700;display:flex;align-items:center;justify-content:center;text-transform:uppercase}

/* hero */
.hero{left:0;top:24px;width:1200px;height:650px;background:linear-gradient(90deg,#f3f4f5 0%,#eceff2 45%,#e5e8ec 100%);overflow:hidden}
.hero-photo{position:absolute;left:480px;top:0;width:720px;height:650px;background:radial-gradient(ellipse at 55% 40%,#d9c4b4 0%,#cdd6e3 35%,#e3e7ee 70%,#eef0f3 100%)}
.site-nav{position:absolute;top:36px;font-size:10.5px;font-weight:800;text-transform:uppercase;color:var(--ink);display:flex;gap:20px}
.site-nav .active{color:var(--brand)}
.nav-left{left:122px}
.nav-right{left:763px;align-items:center}
.social-dot{display:inline-block;width:10px;height:10px;border:1.5px solid var(--ink);border-radius:50%}
.brand-mark{position:absolute;left:480px;top:22px;width:240px;text-align:center;color:var(--brand)}
.brand-mark .name{font-weight:700;font-size:25px;line-height:1.05;text-transform:uppercase;letter-spacing:.5px}
.brand-mark .phone{font-weight:700;font-size:15px;margin-top:6px}
.eyebrow{font-size:12px;font-weight:600;text-transform:uppercase;color:var(--brand);display:flex;align-items:center;gap:4px}
.eyebrow .rule{display:inline-block;width:72px;height:1px;background:var(--brand)}
.hero .eyebrow{position:absolute;left:122px;top:182px}
.hero-title{position:absolute;left:120px;top:200px;font-size:59px;font-weight:900;line-height:57px;color:var(--ink);text-transform:uppercase;letter-spacing:-.5px}
.hero-title em{font-style:normal;color:var(--brand)}
.hero-lede{position:absolute;left:122px;top:432px;width:410px;font-size:13.5px;line-height:19px;color:var(--ink)}

/* alkaline */
.jugs-photo{left:120px;top:720px;width:510px;height:520px;border-radius:30px;background:radial-gradient(ellipse at 50% 55%,#8fb3e3 0%,#b7cdec 40%,#e4edf8 70%,#ffffff 100%)}
.section-title{font-weight:900;text-transform:uppercase;color:var(--brand);letter-spacing:-.2px}
.alkaline-title{left:697px;top:794px;font-size:41px;line-height:42px}
.body-copy{font-size:12px;line-height:19px;color:var(--text)}
.alkaline-copy{left:697px;top:935px;width:392px}
.alkaline-copy p+p{margin-top:18px}

/* watermark */
.watermark{left:0;width:1200px;white-space:nowrap;overflow:hidden;font-weight:900;font-size:98px;line-height:1;text-transform:uppercase;letter-spacing:-1px}
.watermark-light{top:1280px;height:77px;color:var(--pale)}

/* about */
.about-panel{left:0;top:1357px;width:600px;height:468px;background:var(--brand);color:var(--white)}
.about-photo{left:600px;top:1357px;width:600px;height:468px;background:linear-gradient(180deg,#c9c6c0 0%,#b8b5ae 45%,#d3c9b9 70%,#c9bba6 100%)}
.about-title{position:absolute;left:121px;top:58px;font-size:41px;line-height:43px;font-weight:900;text-transform:uppercase}
.about-sub{position:absolute;left:122px;top:196px;font-size:12px;font-weight:800;text-transform:uppercase}
.about-copy{position:absolute;left:122px;top:230px;width:400px;font-size:12px;line-height:19px;color:var(--white)}
.about-panel .btn{left:122px;top:363px;width:187px;height:40px;background:#1d1f2a}

/* products */
.products-title{left:0;top:1866px;width:1200px;text-align:center;font-size:40px}
.product{position:absolute;top:1929px;width:307px;text-align:center}
.product .disc{width:307px;height:307px;border-radius:50%}
.product h3{margin-top:14px;font-size:19px;line-height:23px;font-weight:900;text-transform:uppercase;color:var(--ink)}
.disc-qzrv{background:radial-gradient(circle at 50% 55%,#b9b3aa 0%,#6e6a66 55%,#3d3c3c 100%)}
.disc-supplies{background:linear-gradient(180deg,#dfe6ef 0%,#4a4f58 35%,#2c2f36 75%,#dcdcdc 100%)}
.disc-ice{background:linear-gradient(90deg,#5c6068 0%,#c9d3df 25%,#e9eef4 55%,#c4ceda 80%,#4e525a 100%)}

/* aluminum */
.aluminum{left:0;top:2336px;width:1200px;height:737px;background:linear-gradient(180deg,#ffffff 0%,#ffffff 30%,#d8d9dd 50%,#7f7a74 70%,#c9ccd4 85%,#e6e9ef 100%)}
.aluminum .eyebrow{position:absolute;left:0;top:54px;width:1200px;justify-content:center;gap:6px}
.aluminum .eyebrow .rule{width:74px}
.aluminum-title{position:absolute;left:0;top:66px;width:1200px;text-align:center;font-size:52px;line-height:57px;font-weight:900;text-transform:uppercase;color:var(--ink)}
.aluminum-title em{font-style:normal;color:var(--brand)}
.aluminum-lede{position:absolute;left:0;top:186px;width:1200px;text-align:center;font-size:12.5px;color:var(--text)}
.aluminum .btn{left:507px;top:215px;width:186px;height:40px}

/* footer */
.footer{left:0;top:3073px;width:1200px;height:363px;background:var(--footer);color:var(--white);overflow:hidden}
.footer-brand{position:absolute;left:120px;top:44px;width:180px;text-align:center;color:var(--brand)}
.footer-brand .name{font-weight:700;font-size:24px;line-height:1.05;text-transform:uppercase}
.footer-brand .phone{font-weight:700;font-size:14px;margin-top:8px}
.footer-col{position:absolute;top:30px;font-size:11.5px;line-height:17.5px}
.footer-col h4{font-size:12.5px;font-weight:900;text-transform:uppercase;margin-bottom:8px}
.footer-col ul{list-style:none}
.footer-col p+p{margin-top:17px}
.news-input{margin-top:14px;width:243px;height:39px;border:1px solid #b7b9c2;border-radius:20px;padding-left:20px;display:flex;align-items:center;font-size:10px;color:#d8d9de}
.news-btn{margin-top:8px;width:243px;height:40px;border-radius:20px;background:var(--brand);display:flex;align-items:center;justify-content:center;font-weight:900;font-size:11px;text-transform:uppercase}
.footer-rule{position:absolute;left:122px;top:228px;width:956px;height:1px;background:var(--footer-line)}
.footer-copy{position:absolute;left:122px;top:252px;font-size:11.5px}
.footer-social{position:absolute;left:561px;top:240px;display:flex;gap:11px}
.footer-social span{width:33px;height:33px;border:1px solid #cfd0d6;border-radius:50%;display:flex;align-items:center;justify-content:center}
.footer-social span i{width:7px;height:7px;border-radius:50%;background:#fff}
.footer-legal{position:absolute;left:846px;top:252px;font-size:11.5px;display:flex;gap:13px}
.watermark-dark{top:280px;height:83px;color:#2d2f3a}
</style>
</head>
<body>

<div class="abs promo-bar">Refill more, pay less – ask about our monthly plans.</div>

<header class="abs hero">
  <div class="hero-photo" role="img" aria-label="Woman in a striped shirt drinking a glass of water at home, large faint water-drop shape behind her"></div>
  <nav class="site-nav nav-left">
    <span class="active">Home</span><span>About Us</span><span>Our Products</span><span>Why Aluminum</span>
  </nav>
  <div class="brand-mark">
    <div class="name">Brookvale<br>Refill Den</div>
    <div class="phone">555-014-2290</div>
  </div>
  <nav class="site-nav nav-right">
    <span>Wellness Blog</span><span>Contact Us</span>
    <span style="display:flex;align-items:center;gap:6px">
      <svg width="16" height="13" viewBox="0 0 16 13"><path d="M0 1h3l2 7h8l2-5H5" fill="none" stroke="#16171c" stroke-width="1.6"/><circle cx="6" cy="11" r="1.3" fill="#16171c"/><circle cx="12" cy="11" r="1.3" fill="#16171c"/></svg>Cart (0)
    </span>
    <span class="social-dot"></span><span class="social-dot"></span>
  </nav>
  <div class="eyebrow">Pure water, stronger community <span class="rule"></span></div>
  <h1 class="hero-title">Elevate your<br><em>hydration.</em><br>Empower the<br>planet.</h1>
  <p class="hero-lede">Premium alkaline water in refillable aluminum bottles — made for active, eco-conscious lifestyles.</p>
  <a class="btn" style="left:123px;top:484px;width:144px;height:39px">Shop Now</a>
</header>

<section>
  <div class="abs jugs-photo" role="img" aria-label="Three blue five-gallon water jugs with water splashing around them"></div>
  <h2 class="abs section-title alkaline-title">Alkaline and<br>purified drinking<br>water</h2>
  <div class="abs body-copy alkaline-copy">
    <p>Brookvale Canteen Works bottles ultra-purified alkaline water that is pH 9+ to support optimal hydration and whole-body wellness. Alkaline water is believed to help neutralize acid in the body, improve hydration at the cellular level, and support athletic performance and recovery.</p>
    <p>Every drop is filtered through a multi-stage process to remove impurities and enhance mineral content, ensuring a crisp, clean taste with every sip.</p>
  </div>
  <a class="btn" style="left:697px;top:1124px;width:188px;height:41px">Want to know more</a>
</section>

<div class="abs watermark watermark-light" aria-hidden="true">Sustainable Hydration</div>

<section>
  <div class="abs about-panel">
    <h2 class="about-title">Purpose-driven<br>bottled water<br>brand</h2>
    <p class="about-sub">We don’t just do business here, we live here too.</p>
    <p class="about-copy">At Brookvale Canteen Works, hydration goes far beyond simply quenching thirst; it represents a deep commitment to enhancing both personal health and environmental sustainability. Drawing inspiration from the resilient and vibrant spirit of Brookvale, CO, the brand delivers a premium alkaline water experience thoughtfully designed to meet the needs of today’s health-conscious and eco-aware consumers.</p>
    <a class="btn">More about our water</a>
  </div>
  <div class="abs about-photo" role="img" aria-label="Family of seven standing together on a beach in summer clothes"></div>
</section>

<section>
  <h2 class="abs section-title products-title">What we are selling?</h2>
  <div class="product" style="left:122px">
    <div class="disc disc-qzrv" role="img" aria-label="Boxes of QZRV electrolyte drink mix held in hand"></div>
    <h3>QZRV Products</h3>
  </div>
  <div class="product" style="left:447px">
    <div class="disc disc-supplies" role="img" aria-label="Store wall of tumblers, water jugs and dispensers"></div>
    <h3>Supplies for water<br>refilling</h3>
  </div>
  <div class="product" style="left:772px">
    <div class="disc disc-ice" role="img" aria-label="Freezer case stocked with bags of ice"></div>
    <h3>Ice</h3>
  </div>
</section>

<section class="abs aluminum" role="img" aria-label="Store owners smiling behind rows of white aluminum water bottles in the shop">
  <div class="eyebrow"><span class="rule"></span> Why choose aluminum? <span class="rule"></span></div>
  <h2 class="aluminum-title">It’s the future of<br><em>bottled</em> water.</h2>
  <p class="aluminum-lede">Our bottles are designed to be refilled again and again — built for durability and made to go the distance with you.</p>
  <a class="btn">Want to know more</a>
</section>

<footer class="abs footer">
  <div class="footer-brand">
    <div class="name">Brookvale<br>Refill Den</div>
    <div class="phone">555-014-2290</div>
  </div>
  <div class="footer-col" style="left:366px">
    <h4>Quick Links</h4>
    <ul><li>Home</li><li>About Us</li><li>Our Products</li><li>Why Aluminum</li><li>Blog</li></ul>
  </div>
  <div class="footer-col" style="left:553px">
    <h4>Get in touch</h4>
    <p>Location: 4820 W. Alderbrook Rd., Ste. 210<br>Brookvale, CO 80910</p>
    <p>Hours: Tuesday–Friday 9am–6pm<br>Saturday &amp; Sunday 10am–5pm<br>Closed on Mondays</p>
    <p>Phone: (555) 014-2290</p>
  </div>
  <div class="footer-col" style="left:834px;width:260px">
    <h4>Newsletter</h4>
    <p>Drop your email address to receive news and Offers. No spam (scout’s honor)</p>
    <div class="news-input">Enter your email...</div>
    <div class="news-btn">Subscribe</div>
  </div>
  <div class="footer-rule"></div>
  <div class="footer-copy">© copyrights 2026 brookvalecanteenworks.com</div>
  <div class="footer-social"><span><i></i></span><span><i></i></span></div>
  <div class="footer-legal"><span>Terms of Use</span><span>Privacy Policy</span><span>Disclaimer</span></div>
  <div class="abs watermark watermark-dark" aria-hidden="true">Sustainable Hydration</div>
</footer>

</body>
</html>
```